Brimvane.com fiber optic internet website redesign

We need a new website design for our fiber optic internet company that provides internet, phone, and tv services. It should use the text "Marrowfen fiber optics", and "I beamed up with Marrowfen". The design should use the color blue and the attached logo.
We are a 30 year old internet company who started as a dial up internet provider in our basement. Today we design, build, and maintain our own fiber optic internet network to provide service to residential, business, educational, healthcare, and governmental customers

```html
<!DOCTYPE html>
<html lang="en">
<head>
<meta charset="UTF-8">
<title>Brimvane – Marrowfen Fiber Optics</title>
<link href="https://fonts.googleapis.com/css2?family=Figtree:wght@400;500;600;700;800&display=swap" rel="stylesheet">
<style>
  :root {
    --brand-blue: #1a4fa0;
    --brand-blue-deep: #0f3f8c;
    --ink: #111418;
    --ink-soft: #2a2f36;
    --page-bg: #f2f3f5;
    --header-bg: #ffffff;
    --line: #e3e5e9;
    --card-top: #ffffff;
    --card-bottom: #eef1f6;
    --hero-dark: #0b2a55;
    --hero-mid: #1c5d9c;
    --hero-light: #4fb6f0;
  }
  * { box-sizing: border-box; margin: 0; padding: 0; }
  html, body {
    width: 1200px; height: 750px; overflow: hidden;
    background: var(--page-bg);
    font-family: "Figtree", sans-serif;
    color: var(--ink);
  }
  .site-header {
    height: 86px; background: var(--header-bg);
    border-bottom: 1px solid var(--line);
    display: flex; align-items: center;
    padding: 0 130px;
  }
  .brand { display: flex; align-items: center; gap: 10px; width: 178px; }
  .brand-dot { width: 32px; height: 32px; border-radius: 50%; background: var(--brand-blue); }
  .brand-name { font-size: 27px; font-weight: 700; color: var(--ink); letter-spacing: -0.3px; }
  .main-nav { display: flex; gap: 46px; font-size: 15px; font-weight: 500; color: var(--ink-soft); }
  .main-nav span { display: flex; align-items: center; gap: 6px; }
  .btn {
    display: inline-flex; align-items: center; justify-content: center; gap: 10px;
    border-radius: 4px; font-weight: 600; font-family: inherit;
  }
  .btn-primary { background: var(--brand-blue); color: #fff; }
  .header-cta { margin-left: auto; height: 38px; padding: 0 18px; font-size: 14px; }
  .hero {
    display: flex; gap: 57px;
    padding: 50px 95px 0;
  }
  .hero-visual {
    width: 389px; height: 476px; border-radius: 6px; flex-shrink: 0;
    background:
      radial-gradient(ellipse at 50% 92%, var(--hero-light) 0%, rgba(79,182,240,0) 45%),
      linear-gradient(180deg, #3f8fd0 0%, var(--hero-mid) 40%, var(--hero-dark) 100%);
  }
  .hero-content { padding-top: 20px; }
  .hero-title { font-size: 50px; font-weight: 800; line-height: 1.15; letter-spacing: -0.5px; }
  .hero-title .accent { color: var(--brand-blue); }
  .hero-lead { margin-top: 18px; font-size: 17px; font-weight: 500; color: var(--ink); }
  .hero-actions { display: flex; gap: 18px; margin-top: 30px; }
  .hero-actions .btn { height: 48px; font-size: 16px; }
  .hero-actions .btn-primary { width: 130px; }
  .btn-outline {
    width: 163px; font-size: 14px; color: var(--brand-blue-deep);
    border: 1.5px solid #8fa9d4; background: #fff;
  }
  .service-cards { display: flex; gap: 27px; margin-top: 58px; }
  .service-card {
    position: relative; width: 170px; height: 155px;
    background: linear-gradient(180deg, var(--card-top), var(--card-bottom));
    border-radius: 4px;
    box-shadow: 0 2px 8px rgba(20,40,80,0.08);
    display: flex; flex-direction: column; align-items: center; justify-content: flex-end;
    padding-bottom: 18px;
  }
  .service-card .corner-arrow { position: absolute; top: 12px; right: 12px; }
  .service-card .icon { margin-bottom: 18px; }
  .service-label { font-size: 12.5px; font-weight: 600; color: var(--ink); }
</style>
</head>
<body>
  <header class="site-header">
    <div class="brand">
      <span class="brand-dot"></span>
      <span class="brand-name">brimvane</span>
    </div>
    <nav class="main-nav">
      <span>Home</span>
      <span>Services
        <svg width="9" height="6" viewBox="0 0 9 6"><path d="M1 1l3.5 3.5L8 1" fill="none" stroke="currentColor" stroke-width="1.4"/></svg>
      </span>
      <span>About</span>
      <span>Contact</span>
    </nav>
    <a class="btn btn-primary header-cta">Order Now
      <svg width="7" height="10" viewBox="0 0 7 10"><path d="M1.5 1l4 4-4 4" fill="none" stroke="#fff" stroke-width="1.5"/></svg>
    </a>
  </header>

  <main class="hero">
    <div class="hero-visual" role="img" aria-label="City skyline at night with glowing blue fiber optic light trails"></div>

    <section class="hero-content">
      <h1 class="hero-title">Get Lit with <span class="accent">Marrowfen</span><br>Fiber Optics</h1>
      <p class="hero-lead">Internet, Phone, and TV Services That Keep You Connected.</p>
      <div class="hero-actions">
        <a class="btn btn-primary">Order Now</a>
        <a class="btn btn-outline">Check Availability</a>
      </div>

      <div class="service-cards">
        <div class="service-card">
          <svg class="corner-arrow" width="20" height="20" viewBox="0 0 20 20"><path d="M3 17L17 3M7 3h10v10" fill="none" stroke="#111" stroke-width="1.8"/></svg>
          <svg class="icon" width="66" height="54" viewBox="0 0 66 54" fill="none" stroke="#1a4fa0" stroke-width="3">
            <rect x="4" y="22" width="16" height="28"/><rect x="22" y="12" width="18" height="38"/><rect x="42" y="4" width="18" height="46"/>
            <path d="M9 30h6M9 38h6M27 20h8M27 28h8M27 36h8M47 12h8M47 20h8M47 28h8M47 36h8M1 50h64"/>
          </svg>
          <span class="service-label">Residential Services</span>
        </div>
        <div class="service-card">
          <svg class="corner-arrow" width="20" height="20" viewBox="0 0 20 20"><path d="M3 17L17 3M7 3h10v10" fill="none" stroke="#111" stroke-width="1.8"/></svg>
          <svg class="icon" width="62" height="58" viewBox="0 0 62 58" fill="none" stroke="#1a4fa0" stroke-width="3">
            <path d="M6 54V12l22-8v50M28 24h24v30M2 54h58"/>
            <path d="M14 18v30M21 15v33M36 32v16M44 32v16"/>
          </svg>
          <span class="service-label">Business Services</span>
        </div>
        <div class="service-card">
          <svg class="corner-arrow" width="20" height="20" viewBox="0 0 20 20"><path d="M3 17L17 3M7 3h10v10" fill="none" stroke="#111" stroke-width="1.8"/></svg>
          <svg class="icon" width="56" height="60" viewBox="0 0 56 60" fill="none" stroke="#1a4fa0" stroke-width="3">
            <circle cx="28" cy="18" r="4"/>
            <path d="M18 28a14 14 0 0 1 0-20M38 28a14 14 0 0 0 0-20M12 34a22 22 0 0 1 0-32M44 34a22 22 0 0 0 0-32"/>
            <path d="M28 22L16 58M28 22l12 36M20 46h16M23 36h10"/>
          </svg>
          <span class="service-label">Packages</span>
        </div>
      </div>
    </section>
  </main>
</body>
</html>
```